'Tarovin' a financial/crypto-currency exchange in the middle east

On the card we need 1) Name 2) title 3) email address 4) phone number using the same colors and theme as the logo. On one side we just want the logo and we want the whole card to be in blue (same blue as logo) with the logo in the back being white.
Industry/Entity Type
Financial

```html
<!DOCTYPE html>
<html lang="en">
<head>
<meta charset="utf-8">
<title>Tarovin Business Card</title>
<link href="https://fonts.googleapis.com/css2?family=Montserrat:wght@600;700&family=Questrial&display=swap" rel="stylesheet">
<style>
  :root {
    --brand-blue: #2a7fc1;
    --brand-blue-soft: #3a8ccc;
    --brand-blue-deep: #216ca6;
    --paper-white: #f4f4f2;
    --divider-grey: #3b3f45;
    --backdrop: #2e2e2e;
    --ink-white: #ffffff;
  }
  * { margin: 0; padding: 0; box-sizing: border-box; }
  html, body { width: 799px; height: 1200px; overflow: hidden; background: var(--backdrop); }
  .canvas {
    width: 799px; height: 1200px; position: relative;
    display: flex; flex-direction: column; align-items: center; justify-content: center; gap: 110px;
  }
  .card {
    width: 640px; height: 366px; border-radius: 26px; position: relative; overflow: hidden;
  }
  /* Front */
  .card-front { background: var(--brand-blue); }
  .front-texture {
    position: absolute; inset: 0;
    background: radial-gradient(circle at 50% 50%, var(--brand-blue-soft), var(--brand-blue) 70%);
  }
  .front-brand {
    position: absolute; inset: 0; display: flex; align-items: center; justify-content: center; gap: 20px;
  }
  .brand-dot {
    width: 82px; height: 82px; border-radius: 50%; background: var(--ink-white);
  }
  .brand-name {
    font-family: "Montserrat", sans-serif; font-weight: 700; font-size: 66px;
    color: var(--ink-white); letter-spacing: 1px;
  }
  /* Back */
  .card-back { background: var(--brand-blue); }
  .back-shape { position: absolute; inset: 0; }
  .back-decor { position: absolute; left: 40px; top: 30px; width: 300px; height: 300px; border-radius: 50%; background: var(--brand-blue-deep); opacity: .35; }
  .holder {
    position: absolute; left: 44px; top: 44px; color: var(--ink-white);
  }
  .holder-name { font-family: "Montserrat", sans-serif; font-weight: 700; font-size: 25px; }
  .holder-title { font-family: "Questrial", sans-serif; font-size: 14px; margin-top: 2px; }
  .contacts {
    position: absolute; left: 44px; bottom: 46px; list-style: none;
    font-family: "Questrial", sans-serif; font-size: 16px; color: var(--ink-white);
  }
  .contacts li { display: flex; align-items: center; gap: 12px; line-height: 26px; }
  .contacts svg { width: 14px; height: 14px; fill: var(--ink-white); flex: none; }
  .back-brand {
    position: absolute; right: 58px; top: 0; bottom: 0;
    display: flex; align-items: center; gap: 18px;
  }
  .back-brand .brand-dot { width: 92px; height: 92px; background: var(--brand-blue); }
  .back-brand .brand-name {
    writing-mode: vertical-rl; font-size: 56px; color: var(--brand-blue);
  }
</style>
</head>
<body>
<main class="canvas">
  <section class="card card-front" aria-label="Card front">
    <div class="front-texture" role="img" aria-label="Faint repeating brand pattern across the blue card"></div>
    <div class="front-brand">
      <span class="brand-dot"></span>
      <span class="brand-name">Tarovin</span>
    </div>
  </section>

  <section class="card card-back" aria-label="Card back">
    <div class="back-decor" role="img" aria-label="Large faint brand mark in the background"></div>
    <svg class="back-shape" viewBox="0 0 640 366" preserveAspectRatio="none">
      <path d="M392 0 Q300 183 370 366 L640 366 L640 0 Z" fill="var(--divider-grey)"/>
      <path d="M408 0 Q318 183 384 366 L640 366 L640 0 Z" fill="var(--paper-white)"/>
    </svg>
    <div class="holder">
      <p class="holder-name">Tarovin Halden</p>
      <p class="holder-title">Managing Director</p>
    </div>
    <ul class="contacts">
      <li><svg viewBox="0 0 16 16"><path d="M3 1h3l1.5 4-2 1.3a9 9 0 0 0 4.2 4.2L11 8.5l4 1.5v3a2 2 0 0 1-2 2A13 13 0 0 1 1 3a2 2 0 0 1 2-2z"/></svg>555.014.2290</li>
      <li><svg viewBox="0 0 16 16"><path d="M1 3h14v10H1z M2 4l6 5 6-5" stroke="#2a7fc1" stroke-width="1"/></svg>tarovin@tarovinexchange.com</li>
      <li><svg viewBox="0 0 16 16"><circle cx="8" cy="8" r="7"/><path d="M1 8h14M8 1v14M8 1c-3 3-3 11 0 14M8 1c3 3 3 11 0 14" stroke="#2a7fc1" stroke-width="1" fill="none"/></svg>www.tarovinexchange.com</li>
    </ul>
    <div class="back-brand">
      <span class="brand-dot"></span>
      <span class="brand-name">Tarovin</span>
    </div>
  </section>
</main>
</body>
</html>
```